NEW YORK Plumbing/utility company 10 year anniversary business card

Looking For simple back and front business card would like to include a few things in description
We offer 24/7 emergency service
residential
commercial
industrial
municipal
services offered
Plumbing
hydro excavation
hydro jetting
Well pumps
Sewer pumps
water mains
sewer mains

```html
<!DOCTYPE html>
<html lang="en">
<head>
<meta charset="UTF-8">
<title>Ridgeway Water &amp; Sewer – Business Card</title>
<link rel="stylesheet" href="https://fonts.googleapis.com/css2?family=Montserrat:wght@600;700;800&family=Arimo:wght@400;700&display=swap">
<style>
  :root{
    --navy:#1d63a6;
    --sky:#2aa3e0;
    --white:#ffffff;
    --ink:#1f2a36;
    --stage:#e6e8eb;
  }
  *{box-sizing:border-box;margin:0;padding:0}
  html,body{width:1200px;height:900px;overflow:hidden;background:var(--stage)}
  .canvas{width:1200px;height:900px;display:flex;flex-direction:column;align-items:center;justify-content:center;gap:36px}
  .card{width:700px;height:400px;position:relative;overflow:hidden;box-shadow:0 6px 18px rgba(0,0,0,.15)}
  .card::after{content:"";position:absolute;left:0;right:0;bottom:0;height:10px;background:var(--sky)}

  /* front */
  .card--front{background:var(--navy);color:var(--white);display:flex;flex-direction:column;align-items:center;padding-top:62px}
  .brand{display:flex;align-items:center;gap:14px;font-family:"Montserrat",sans-serif;font-weight:800}
  .brand__dot{width:26px;height:26px;border-radius:50%;background:var(--sky)}
  .brand__name{font-size:44px;letter-spacing:1px;line-height:1}
  .brand__sub{font-family:"Montserrat",sans-serif;font-weight:800;font-size:20px;letter-spacing:4px;margin-top:12px;display:flex;align-items:center;gap:12px}
  .brand__sub::before,.brand__sub::after{content:"";width:36px;height:2px;background:currentColor}
  .card--front .brand__sub{color:var(--white)}
  .services{margin-top:44px;width:560px;text-align:center}
  .services__title{font-family:"Montserrat",sans-serif;font-weight:700;font-size:22px;color:var(--sky);letter-spacing:1px;display:flex;align-items:center;gap:18px}
  .services__title::before,.services__title::after{content:"";flex:1;height:2px;background:var(--sky)}
  .services__list{list-style:none;font-family:"Arimo",sans-serif;font-size:19px;margin-top:16px;display:flex;flex-wrap:wrap;justify-content:center;gap:8px 16px}
  .services__list li::before{content:"•";color:var(--sky);margin-right:6px}

  /* back */
  .card--back{background:var(--white);display:grid;grid-template-columns:330px 1fr;grid-template-rows:250px 1fr;padding:40px 36px 0 36px}
  .card--back .brand{color:var(--navy)}
  .card--back .brand__name{font-size:34px}
  .card--back .brand__dot{width:22px;height:22px}
  .card--back .brand__sub{color:var(--navy);font-size:16px;letter-spacing:3px}
  .identity{display:flex;flex-direction:column;align-items:center;justify-content:center;border-right:2px solid var(--navy);margin:20px 0 20px}
  .contact{padding:20px 0 0 34px;font-family:"Arimo",sans-serif;color:var(--ink)}
  .contact__name{font-family:"Montserrat",sans-serif;font-weight:800;font-size:30px;color:var(--navy)}
  .contact__role{font-size:19px;margin-top:4px}
  .contact__list{list-style:none;margin-top:20px;display:flex;flex-direction:column;gap:9px;font-size:18px}
  .contact__list li{display:flex;align-items:center;gap:10px}
  .contact__list svg{width:18px;height:18px;fill:var(--sky)}
  .offer{grid-column:1 / -1;text-align:center;padding-top:8px}
  .offer__head{font-family:"Montserrat",sans-serif;font-weight:700;font-size:26px;color:var(--sky)}
  .offer__sectors{list-style:none;display:flex;justify-content:center;gap:18px;font-family:"Arimo",sans-serif;font-size:21px;color:var(--ink);margin-top:8px}
  .offer__sectors li::before{content:"•";color:var(--sky);margin-right:6px}
</style>
</head>
<body>
<main class="canvas">
  <section class="card card--front" aria-label="Card front">
    <div class="brand"><span class="brand__dot"></span><span class="brand__name">RIDGEWAY</span></div>
    <div class="brand__sub">WATER &amp; SEWER</div>
    <div class="services">
      <h2 class="services__title">SERVICES OFFERED</h2>
      <ul class="services__list">
        <li>Plumbing</li><li>Hydro excavation</li><li>Hydro jetting</li><li>Well pumps</li>
        <li>Sewer pumps</li><li>Water mains</li><li>Sewer mains</li>
      </ul>
    </div>
  </section>

  <section class="card card--back" aria-label="Card back">
    <div class="identity">
      <div class="brand"><span class="brand__dot"></span><span class="brand__name">RIDGEWAY</span></div>
      <div class="brand__sub">WATER &amp; SEWER</div>
    </div>
    <div class="contact">
      <h1 class="contact__name">DANIEL REYES</h1>
      <p class="contact__role">CEO/Founder</p>
      <ul class="contact__list">
        <li><svg viewBox="0 0 24 24"><path d="M6.6 10.8a15 15 0 0 0 6.6 6.6l2.2-2.2c.3-.3.7-.4 1-.2 1.1.4 2.3.6 3.6.6.6 0 1 .4 1 1V20c0 .6-.4 1-1 1A17 17 0 0 1 3 4c0-.6.4-1 1-1h3.5c.6 0 1 .4 1 1 0 1.3.2 2.5.6 3.6.1.3 0 .7-.2 1z"/></svg>845-555-0182</li>
        <li><svg viewBox="0 0 24 24"><path d="M2 5h20v14H2zm2 2v.5l8 5 8-5V7l-8 5z"/></svg>info@ridgewayws.com</li>
        <li><svg viewBox="0 0 24 24"><path d="M12 2a10 10 0 1 0 0 20 10 10 0 0 0 0-20zm6.9 9h-3a15 15 0 0 0-1.3-5.6A8 8 0 0 1 18.9 11zM12 4c.9 1.2 1.8 3.6 1.9 7h-3.8c.1-3.4 1-5.8 1.9-7zM9.4 5.4A15 15 0 0 0 8.1 11h-3a8 8 0 0 1 4.3-5.6zM5.1 13h3a15 15 0 0 0 1.3 5.6A8 8 0 0 1 5.1 13zM12 20c-.9-1.2-1.8-3.6-1.9-7h3.8c-.1 3.4-1 5.8-1.9 7zm2.6-1.4a15 15 0 0 0 1.3-5.6h3a8 8 0 0 1-4.3 5.6z"/></svg>www.ridgewayws.com</li>
      </ul>
    </div>
    <div class="offer">
      <p class="offer__head">We offer 24/7 emergency service</p>
      <ul class="offer__sectors"><li>Residential</li><li>Commercial</li><li>Industrial</li><li>Municipal</li></ul>
    </div>
  </section>
</main>
</body>
</html>
```